KVR Associates needs a web site

We need a web site for www.kvrassociates-example.com. KVR is a mergers and acquisition consulting company that focuses our buyer and seller services on logistics companies. We help put companies together, and help with legal and financial due diligence. We want the web site to express our service and show the logistics components. We want personalized images versus pictures of trucks and airplanes.

Our new logo uses Burgandy and grey colors. Image attached. We are not in to bold, big letters...classy, artistic, low key preferred. Confidentiality, experience, professional are what we want to express on the site.

All we expect for the first part of this project is a home page, and one subpage.  We are budgeting other funds for the technical aspects of the web site

Reason: All that I'm seeing so far is trucks, forklifts and planes. We are a legal mergers and acquisitions firm that focus on logistics. I like some of the images to say logistics, but really want it say legal, financial, and putting companies together. Will pay extra for the sub page if someone can impress us with a home page.

Reason: Swamped with another project at the moment...will work on this over the weekend and provide designer feedback and select final design by Tuesday

```html
<!DOCTYPE html>
<html lang="en">
<head>
<meta charset="utf-8">
<title>KVR Associates</title>
<link href="https://fonts.googleapis.com/css2?family=Open+Sans:wght@300;400;600&display=swap" rel="stylesheet">
<style>
:root{
  --header-bg:#2d2e34;
  --page-bg:#e9ebef;
  --card:#ffffff;
  --burgundy:#8e1b3e;
  --blue:#2a8bcb;
  --icon-grey:#6d6f74;
  --body-text:#9a9ca0;
  --rule:#d8dadd;
  --client-grey:#c2c3c5;
  --footer-bg:#2b2c31;
  --footer-text:#e6e6e6;
  --green:#2fae6e;
  --orange:#ec6b1f;
  --gold:#f1a82a;
}
*{margin:0;padding:0;box-sizing:border-box}
html,body{width:1120px;height:1200px;overflow:hidden;background:var(--page-bg);font-family:"Open Sans",Arial,sans-serif}
.page{position:relative;width:1120px;height:1200px;overflow:hidden}
.site-header{position:absolute;left:0;top:0;width:1120px;height:464px;background:var(--header-bg)}
.brand{position:absolute;left:90px;top:27px;width:233px;height:82px;background:var(--card);display:flex;align-items:center;padding-left:18px;gap:10px}
.brand-mark{width:14px;height:14px;background:var(--burgundy)}
.brand-name{font-size:21px;font-weight:600;color:var(--burgundy);letter-spacing:.3px}
.main-nav{position:absolute;left:533px;top:0;display:flex;gap:16px}
.nav-item{width:112px;height:112px;background:var(--card);display:flex;flex-direction:column;align-items:center;padding-top:28px;font-size:11px;color:var(--burgundy);text-decoration:none;position:relative}
.nav-item svg{width:36px;height:34px;margin-bottom:14px}
.nav-item.is-active{height:116px;border-bottom:4px solid #7d7f84}
.nav-item.is-active::before{content:"";position:absolute;top:0;left:50%;margin-left:-6px;border:6px solid transparent;border-top-color:var(--header-bg)}
.hero{position:absolute;left:91px;top:128px;width:938px;height:336px;display:flex}
.hero-visual{width:641px;height:336px;background:linear-gradient(160deg,#6b5a3f 0%,#a99572 30%,#5a6fb8 48%,#d9dbe0 62%,#8b7a5e 85%,#4a3e30 100%)}
.hero-panel{position:relative;width:297px;height:336px;background:var(--card);padding:36px 24px 0 24px}
.hero-kicker{display:flex;align-items:center;gap:10px;font-size:19px;color:var(--burgundy);padding-bottom:8px;border-bottom:1px solid var(--rule)}
.hero-title{margin-top:12px;font-size:32px;font-weight:300;color:var(--blue);white-space:nowrap}
.hero-text{margin-top:10px;font-size:11.5px;line-height:16px;color:var(--body-text)}
.btn{display:inline-block;margin-top:40px;width:111px;height:36px;line-height:36px;text-align:center;background:var(--blue);color:#fff;font-size:15px;text-decoration:none}
.slider-dots{position:absolute;right:10px;bottom:12px;display:flex;gap:7px}
.dot{width:14px;height:14px;border-radius:50%;border:1px solid #c9cbce}
.dot.is-current{background:var(--blue);border-color:var(--blue)}
.card{position:absolute;left:91px;width:935px;background:var(--card)}
.services{top:487px;height:282px;border-top:1px solid var(--rule);border-bottom:1px solid var(--rule)}
.services-visual{position:absolute;left:52px;top:27px;width:217px;height:255px;background:linear-gradient(180deg,#f2f2f4 0%,#dfe1e6 60%,#cfd3da 100%);border-radius:90px 90px 0 0}
.section-title{font-size:20px;font-weight:400;color:var(--burgundy)}
.services .section-title{position:absolute;left:322px;top:42px}
.service{position:absolute;width:300px;display:flex;gap:14px}
.service-icon{flex:none;width:33px;height:33px}
.service h3{font-size:14.5px;font-weight:400;color:var(--burgundy);margin-top:-2px}
.service p{font-size:11.5px;line-height:16px;color:var(--body-text);margin-top:4px}
.clients{top:797px;height:277px}
.clients .section-title{text-align:center;margin-top:19px}
.client-grid{position:absolute;left:0;top:70px;width:935px;display:grid;grid-template-columns:repeat(4,1fr);row-gap:56px;padding:0 20px}
.client{display:flex;align-items:center;justify-content:center;gap:8px;height:46px;font-size:27px;font-weight:600;color:var(--client-grey);white-space:nowrap}
.client-dot{width:16px;height:16px;border-radius:50%;background:var(--client-grey)}
.site-footer{position:absolute;left:0;top:1074px;width:1120px;height:126px;background:var(--footer-bg)}
.footer-nav{position:absolute;left:93px;top:46px;font-size:10px;color:var(--footer-text)}
.footer-legal{position:absolute;left:93px;top:70px;font-size:10px;color:var(--footer-text)}
.social{position:absolute;left:900px;top:44px;display:flex;gap:18px}
.social span{width:30px;height:30px;border-radius:50%;border:2px solid #e8e8e8}
.social .s1{background:#b2242b}.social .s2{background:#2e4a8a}.social .s3{background:#2a8fcf}
</style>
</head>
<body>
<div class="page">
  <header class="site-header">
    <div class="brand"><span class="brand-mark"></span><span class="brand-name">KVR Associates</span></div>
    <nav class="main-nav">
      <a class="nav-item is-active" href="#">
        <svg viewBox="0 0 36 34" fill="var(--icon-grey)"><path d="M18 3 2 17h5v14h8v-9h6v9h8V17h5z"/></svg>HOME</a>
      <a class="nav-item" href="#">
        <svg viewBox="0 0 36 34" fill="none" stroke="var(--icon-grey)" stroke-width="2.4"><path d="M8 2h14l7 7v23H8z"/><path d="M13 14h11M13 19h11M13 24h11"/></svg>ABOUT</a>
      <a class="nav-item" href="#">
        <svg viewBox="0 0 36 34" fill="none" stroke="var(--icon-grey)" stroke-width="2.4"><path d="M24 6H4v25h24V16"/><path d="M14 22l2-6 14-14 4 4-14 14z"/></svg>SERVICE</a>
      <a class="nav-item" href="#">
        <svg viewBox="0 0 36 34" fill="none" stroke="var(--icon-grey)" stroke-width="2.4"><rect x="2" y="6" width="32" height="24"/><path d="M2 6l16 14L34 6"/></svg>CONTACT</a>
    </nav>
    <section class="hero">
      <div class="hero-visual" role="img" aria-label="Photo of a blue passenger jet being serviced inside a maintenance hangar"></div>
      <div class="hero-panel">
        <div class="hero-kicker">
          <svg width="18" height="18" viewBox="0 0 18 18" fill="none" stroke="#c9cbce" stroke-width="1.5"><circle cx="9" cy="9" r="8"/><path d="M5 9h7M9 6l3 3-3 3"/></svg>SERVICES</div>
        <h1 class="hero-title">PERFECT CHOICE</h1>
        <p class="hero-text">Proin gravida nibh vel velit auctor aliquet. Aenean sollicitudin, lorem quis bibendum auctor, nisi elit consequat ipsum. Duis sedt nibh vulputate cursus a sit.</p>
        <a class="btn" href="#">Read More</a>
        <div class="slider-dots"><span class="dot"></span><span class="dot is-current"></span><span class="dot"></span></div>
      </div>
    </section>
  </header>

  <section class="card services">
    <div class="services-visual" role="img" aria-label="Portrait of a smiling businesswoman in a light suit with arms crossed"></div>
    <h2 class="section-title">OUR CORE SERVICES</h2>
    <div class="service" style="left:318px;top:96px">
      <svg class="service-icon" viewBox="0 0 33 33"><circle cx="16.5" cy="16.5" r="15" fill="none" stroke="var(--green)" stroke-width="2"/><path d="M10 20a4 4 0 0 1 1-8 6 6 0 0 1 11 0 4 4 0 0 1 1 8z" fill="var(--green)"/><path d="M16.5 13v6M14 17l2.5 2.5L19 17" stroke="#fff" stroke-width="1.6" fill="none"/></svg>
      <div><h3>Lorem ipsum dolor sit</h3><p>Lorem ipsum dolor sit amet, consectetur adipiscing elit. Phasellus vitae dui ligula.</p></div>
    </div>
    <div class="service" style="left:642px;top:96px">
      <svg class="service-icon" viewBox="0 0 33 33"><circle cx="16.5" cy="16.5" r="15" fill="none" stroke="var(--blue)" stroke-width="2"/><path d="M14 9h5M14.5 9v5l-4 8h12l-4-8V9" fill="none" stroke="var(--blue)" stroke-width="1.8"/><path d="M12 20h9l1.5 2h-12z" fill="var(--blue)"/></svg>
      <div><h3>Etiam eget porttitor enim</h3><p>Lorem ipsum dolor sit amet, consectetur adipiscing elit. Phasellus vitae dui ligula.</p></div>
    </div>
    <div class="service" style="left:318px;top:178px">
      <svg class="service-icon" viewBox="0 0 33 33"><circle cx="16.5" cy="16.5" r="15" fill="none" stroke="var(--orange)" stroke-width="2"/><path d="M11 9v16" stroke="var(--orange)" stroke-width="2"/><path d="M12 10h11l-3 4 3 4H12z" fill="var(--orange)"/></svg>
      <div><h3>Fusce egestas ultricies</h3><p>Lorem ipsum dolor sit amet, consectetur adipiscing elit. Phasellus vitae dui ligula.</p></div>
    </div>
    <div class="service" style="left:642px;top:178px">
      <svg class="service-icon" viewBox="0 0 33 33"><circle cx="16.5" cy="16.5" r="15" fill="none" stroke="var(--gold)" stroke-width="2"/><path d="M16.5 8a6 6 0 0 0-3.5 10.8V21h7v-2.2A6 6 0 0 0 16.5 8z" fill="none" stroke="var(--gold)" stroke-width="1.8"/><path d="M14 23.5h5" stroke="var(--gold)" stroke-width="1.8"/></svg>
      <div><h3>Donec convallis arcu id lectus</h3><p>Lorem ipsum dolor sit amet, consectetur adipiscing elit. Phasellus vitae dui ligula.</p></div>
    </div>
  </section>

  <section class="card clients">
    <h2 class="section-title">OUR CLIENTS</h2>
    <div class="client-grid">
      <div class="client">Hourline</div>
      <div class="client">Leafmark</div>
      <div class="client">Outerform</div>
      <div class="client"><span class="client-dot"></span>Nestlight</div>
      <div class="client">Codewell</div>
      <div class="client"><span class="client-dot"></span>Crafted Works</div>
      <div class="client">Truegrade</div>
      <div class="client">Finetable</div>
    </div>
  </section>

  <footer class="site-footer">
    <div class="footer-nav">HOME &nbsp;•&nbsp; ABOUT &nbsp;•&nbsp; SERVICES &nbsp;•&nbsp; CONTACT</div>
    <div class="footer-legal">Design © 2014. All right reserved &nbsp;•&nbsp; Privacy Policy</div>
    <div class="social"><span class="s1"></span><span class="s2"></span><span class="s3"></span></div>
  </footer>
</div>
</body>
</html>
```